Security based company delivering Sentinel Risk Training to Law Enforcement Agencies Worldwide.

We need a Web design for a company doing business in Washington D.C. We deliver Sentinel Risk Training to Law Enforcement Agencies throughout the world. Our focus is on Improvised Explosive Devices. We train Bomb Technicians and First Responders in all aspects relating to bombings and criminal incidents globally.

Reason: We have uploaded our logo. Thank you.

Target Market(s)

Military and Law Enforcement Personnel from around the world.

Industry/Entity Type

Business

Requirements
Should not have
• Do not include cartoon like characters.

```html
<!DOCTYPE html>
<html lang="en">
<head>
<meta charset="utf-8">
<title>Sentinel Risk Training</title>
<link rel="stylesheet" href="https://fonts.googleapis.com/css2?family=PT+Sans:wght@400;700&family=PT+Sans+Narrow:wght@400;700&display=swap">
<style>
:root{
  --ink:#1c1c1c;
  --text:#4a4a4a;
  --muted:#8a8a8a;
  --band:#e9e9ea;
  --band-line:#d2d2d4;
  --blue:#3f6aa6;
  --blue-dark:#23477c;
  --red:#c8312a;
  --white:#ffffff;
}
*{box-sizing:border-box;margin:0;padding:0}
html,body{width:744px;height:1200px;overflow:hidden;background:var(--white)}
body{font-family:"PT Sans",Arial,sans-serif;color:var(--text);position:relative}
.site-header{height:90px;display:flex;align-items:center;justify-content:space-between;padding:0 0 0 105px}
.brand{font-weight:700;font-size:17px;color:var(--ink)}
.main-nav{display:flex;height:90px;margin-right:60px}
.main-nav a{display:flex;align-items:center;justify-content:center;width:68px;font-size:13px;color:var(--ink);text-decoration:none;border-left:1px solid #e2e2e2}
.main-nav a:first-child{border-left:none}
.main-nav a.active{background:linear-gradient(90deg,#ffffff,#dcdcdc 50%,#ffffff)}
.hero{position:relative;height:272px;border-top:8px solid var(--blue)}
.hero-photo{position:absolute;inset:0;background:linear-gradient(180deg,#c4b8a6 0%,#a99880 50%,#8e7c68 100%)}
.hero-title{position:absolute;right:40px;top:70px;text-align:right;color:var(--ink)}
.hero-title h1{font-family:"PT Sans Narrow",Arial,sans-serif;font-weight:400;font-size:56px;line-height:1}
.hero-title p{font-size:15px;margin-top:4px}
.ied-band{margin-top:8px;height:96px;background:var(--band);border-top:1px solid var(--band-line);border-bottom:1px solid var(--band-line);display:flex;align-items:center;padding:0 40px 0 112px}
.ied-mark{display:flex;align-items:center;gap:10px;padding-right:28px;border-right:1px solid #b9b9bb;height:62px}
.ied-mark strong{font-family:"PT Sans Narrow",Arial,sans-serif;font-weight:400;font-size:42px;color:var(--ink)}
.ied-mark span{font-size:8px;line-height:1.25;color:var(--ink);width:58px}
.ied-band p{font-size:8.5px;line-height:1.35;padding-left:24px;color:var(--muted)}
.content{display:flex;gap:22px;padding:20px 30px 0 90px;height:252px}
.intro{width:270px}
.intro .lead{font-size:13.5px;line-height:1.3;color:var(--ink)}
.intro .body{font-size:8px;line-height:1.4;color:var(--muted);margin-top:10px}
.feature h2{font-size:9px;font-weight:700;color:var(--ink);margin:22px 0 14px}
.feature-photo{width:330px;height:148px;background:linear-gradient(180deg,#b8c0c8 0%,#9a9e98 55%,#7a7a6e 100%)}
.divider{position:relative;height:18px}
.divider::before{content:"";position:absolute;left:0;right:0;top:9px;border-top:1px solid var(--band-line)}
.divider span{position:absolute;left:50%;top:0;width:18px;height:18px;margin-left:-9px;border-radius:50%;background:var(--white);border:1px solid var(--band-line)}
.testimonials{height:150px;background:var(--band);display:flex;align-items:flex-start;padding:18px 40px 0 95px;position:relative}
.testimonials-intro{width:140px}
.testimonials-intro h2{font-size:9px;font-weight:700;color:var(--ink)}
.testimonials-intro p{font-size:8.5px;line-height:1.35;color:var(--ink);margin-top:12px}
.client{width:80px;margin-left:10px;text-align:center}
.client-photo{width:56px;height:60px;margin:0 auto;background:linear-gradient(180deg,#d9d2c8,#b0a698)}
.client p{font-size:6.5px;color:var(--blue);margin-top:4px;line-height:1.3}
.quote{flex:1;font-size:8px;line-height:1.45;color:var(--muted);padding-left:18px}
.slider-dots{position:absolute;right:46px;bottom:24px;display:flex;gap:5px}
.slider-dots i{width:5px;height:5px;border-radius:50%;background:#b9b9bb}
.slider-dots i:first-child{background:#7b7b7d}
.news{display:flex;gap:40px;padding:26px 40px 0 90px;height:220px}
.news-photo{width:258px;height:176px;background:linear-gradient(135deg,#0d1a2b 0%,#1d3556 55%,#4b7fb8 100%)}
.news-body h2{font-size:9px;font-weight:700;color:var(--ink)}
.news-body h3{font-size:13px;font-weight:700;color:var(--ink);margin-top:18px}
.news-body p{font-size:8.5px;line-height:1.4;color:var(--ink);margin-top:8px;width:300px}
.btn{display:inline-block;margin-top:14px;background:var(--red);color:var(--white);font-size:8px;font-weight:700;padding:6px 28px;border-radius:3px;text-decoration:none}
.site-footer{position:absolute;left:0;right:0;bottom:0;height:86px;background:linear-gradient(180deg,var(--blue) 0%,var(--blue-dark) 100%);color:var(--white)}
.footer-nav{position:absolute;left:88px;top:24px;font-size:11px}
.footer-nav a{color:var(--white);text-decoration:none}
.social{position:absolute;right:92px;top:22px;display:flex;gap:4px}
.social span{width:14px;height:14px;border-radius:50%;background:#6b9bd6}
.social span:nth-child(5){background:#c94a3f}
.copyright{position:absolute;right:88px;top:44px;font-size:7px;color:#c9d6ea}
.footer-rule{position:absolute;left:0;right:0;bottom:10px;border-top:1px solid #5a80b8}
</style>
</head>
<body>
<header class="site-header">
  <div class="brand">Sentinel Risk Training</div>
  <nav class="main-nav">
    <a href="#">About</a>
    <a href="#" class="active">Services</a>
    <a href="#">Contact</a>
  </nav>
</header>

<section class="hero">
  <div class="hero-photo" role="img" aria-label="Desert training range photograph"></div>
  <div class="hero-title">
    <h1>High Risk</h1>
    <p>Security Training</p>
  </div>
</section>

<section class="ied-band">
  <div class="ied-mark"><strong>IED</strong><span>Improvised Explosive Devices</span></div>
  <p>Lorem ipsum dolor sit amet, consectetur adipiscing elit, sed do eiusmod tempor incididunt ut labore et dolore magna aliqua. Ut enim ad minim veniam, quis nostrud exercitation ullamco laboris nisi ut aliquip ex ea commodo consequat. Duis aute irure dolor in reprehenderit in voluptate velit esse cillum dolore eu fugiat nulla pariatur.</p>
</section>

<section class="content">
  <div class="intro">
    <p class="lead">Lorem ipsum dolor sit amet, consectetur adipisicing elit, sed do eiusmod tempor incididunt ut labore et dolore magna aliqua. Ut enim ad minim veniam, quis nostrud exercitation ullamco laboris nisi ut aliquip ex ea commodo consequat. Duis aute irure dolor in reprehenderit in voluptate velit esse cillum dolore eu fugiat nulla pariatur.</p>
    <p class="body">Lorem ipsum dolor sit amet, consectetur adipisicing elit, sed do eiusmod tempor incididunt ut labore et dolore magna aliqua. Ut enim ad minim veniam, quis nostrud exercitation ullamco laboris nisi ut aliquip ex ea commodo consequat. Duis aute irure dolor in reprehenderit in voluptate velit esse cillum dolore eu fugiat nulla pariatur.</p>
  </div>
  <div class="feature">
    <h2>Improvised Explosive Devices</h2>
    <div class="feature-photo" role="img" aria-label="Bomb technician in a protective suit at a roadside"></div>
  </div>
</section>

<div class="divider"><span></span></div>

<section class="testimonials">
  <div class="testimonials-intro">
    <h2>CUSTOMER TESTIMONIALS</h2>
    <p>See what our customers are saying about Sentinel Risk Training</p>
  </div>
  <div class="client">
    <div class="client-photo" role="img" aria-label="Client portrait"></div>
    <p>Client Name<br>Agency Name</p>
  </div>
  <p class="quote">Sed ut perspiciatis unde omnis iste natus error sit voluptatem accusantium doloremque laudantium, totam rem aperiam, eaque ipsa quae ab illo inventore veritatis et quasi architecto beatae vitae dicta sunt explicabo. Nemo enim ipsam voluptatem quia voluptas sit aspernatur aut odit aut fugit, sed quia consequuntur magni dolores eos qui ratione voluptatem sequi nesciunt. Neque porro quisquam est, qui dolorem ipsum quia dolor sit amet.</p>
  <div class="slider-dots"><i></i><i></i><i></i></div>
</section>

<section class="news">
  <div class="news-photo" role="img" aria-label="Person in a suit touching a glowing digital interface"></div>
  <div class="news-body">
    <h2>LATEST NEWS</h2>
    <h3>Ut enim ad minim veniam, quis nostrud exercitation</h3>
    <p>Lorem ipsum dolor sit amet, consectetur adipisicing elit, sed do eiusmod tempor incididunt ut labore et dolore magna aliqua. Ut enim ad minim veniam, quis nostrud exercitation ullamco laboris nisi ut aliquip ex ea commodo consequat. Duis aute irure dolor in reprehenderit in voluptate velit esse cillum dolore eu fugiat nulla pariatur.</p>
    <a href="#" class="btn">READ MORE</a>
  </div>
</section>

<footer class="site-footer">
  <div class="footer-nav"><a href="#">About</a> | <a href="#">Services</a> | <a href="#">Contact</a></div>
  <div class="social"><span></span><span></span><span></span><span></span><span></span></div>
  <div class="copyright">Copyright 2014. All Rights Reserved</div>
  <div class="footer-rule"></div>
</footer>
</body>
</html>
```